Integrative Medical Practice Website Redo

I am needing to have our current website redesigned to make it a responsive website to work on smartphones.
Current website
www.brightoakfm.com
Here are several examples of what I am looking for
https://www.corvanhealth.com/
I am wanting a popup for a newsletter signup
Looking for a very professional, clean, simple, minimalist, bold well designed website
Colors would ideally be greens and blues, cool tones, muted colors, or graytones like:
https://journeybright.org/
Several other clean design examples
http://7harborsrenton.com/
http://www.belvomedical.com/
http://sunpathyouth.com/
http://yourcellduke.com/
I would like the top navigation bar to be able to slide down while browsing site
We are also needing to add several features that are not on our current website:
Questionnaire buttons
Are you toxic questionnaire?
Take our hormone quiz to find out if hormones are affecting your health.
online scheduling option for:
nutrition counselling
testing like body composition, basal metabolic rate, CIMT, breast thermography, VO2 Max testing, Vita Trace
Therapies like whole body vibration, infrared sauna, Exercise with oxygen, hyperbaric oxygen, spinal decompression
Need to have separate page for different services and split up services into:
Consults/Office Visits, Testing, Therapies, Procedures
Need to have a button link to patient portal
Needs to have online store
Need to add navigation button "Start Here"
Need a spot for a video on practice summary
Newsletter signup to collect emails
Testimonials from linkpage
Blog that posts can be shared with social media
Password protected patient access that can integrate into crate.net ideally
Modules for programs online classes/videos
I have attached stock images that you can use, but feel free to find others to use.
I have also attached a copy of our current brochure that shows an overview of the practice
Target Market(s)
Health conscious people of all ages looking for a family medicine doctor
Industry/Entity Type
Alternative Medicine
Coding
Coded - Design and coding required
Number of Pages Required
5+ page
Look and feel

```html
<!DOCTYPE html>
<html lang="en">
<head>
<meta charset="utf-8">
<title>Bright Oak Family Medicine</title>
<link href="https://fonts.googleapis.com/css2?family=Cinzel:wght@400;700&family=Open+Sans:wght@400;600;700&display=swap" rel="stylesheet">
<style>
:root{
  --blue:#2aa3d8;
  --blue-dark:#1b7fb0;
  --green:#8cc63f;
  --green-dark:#5f9a22;
  --ink:#333;
  --muted:#666;
  --light:#f0f0f0;
  --line:#dcdcdc;
  --white:#fff;
}
*{box-sizing:border-box;margin:0;padding:0}
html,body{width:1200px;height:3191px;overflow:hidden;background:var(--white)}
body{font-family:"Open Sans",Arial,sans-serif;color:var(--ink);position:relative}
.abs{position:absolute}
.topbar{left:0;top:0;width:1200px;height:30px;background:var(--blue);color:var(--white);font-size:12px;font-weight:600}
.topbar .phone{left:115px;top:7px}
.topbar .contact{left:245px;top:7px}
.topbar .sep{left:228px;top:6px}
.topbar .cart{right:115px;top:6px}
.header{left:0;top:30px;width:1200px;height:90px;background:var(--white)}
.brand{left:118px;top:18px;display:flex;align-items:center;gap:10px}
.brand .dot{width:34px;height:34px;border-radius:50%;background:var(--green)}
.brand .name{font-family:"Open Sans",sans-serif;font-weight:700;font-size:30px;color:var(--blue-dark);line-height:1}
.brand .tag{font-size:10px;letter-spacing:3px;color:var(--blue-dark);font-weight:700;margin-top:4px}
.nav{left:415px;top:30px;display:flex;gap:16px;font-size:12.5px;font-weight:600;color:var(--muted)}
.nav .active{color:var(--blue);border-bottom:2px solid var(--blue);padding-bottom:4px}
.hero{left:0;top:120px;width:1200px;height:545px;background:linear-gradient(100deg,#c9ccd0 0%,#e9e6e4 35%,#e7cdbd 60%,#d9b19c 80%,#b8a59b 100%)}
.hero h1{left:370px;top:80px;font-family:"Cinzel",serif;font-weight:400;color:var(--blue-dark);font-size:42px;line-height:1.15}
.hero h1 span{display:block;color:#1f5c8a}
.hero .arrow{top:255px}
.hero .dots{left:560px;top:518px;display:flex;gap:8px}
.hero .dots i{width:8px;height:8px;border-radius:50%;background:rgba(255,255,255,.7);display:block}
.hero .dots i:first-child{background:var(--white)}
.questions{left:0;top:665px;width:1200px;height:155px;background:var(--light)}
.questions h2{width:1200px;text-align:center;top:22px;font-family:"Cinzel",serif;font-weight:400;font-size:32px;color:var(--blue-dark)}
.questions .down{left:583px;top:78px}
.booking{left:118px;top:800px;width:967px;height:78px;background:linear-gradient(90deg,#1d86b8,#3fb2d9 55%,#8ccf6a);border:3px solid #d9ecf5}
.booking .text{left:40px;top:20px;font-size:27px;font-weight:700;color:var(--white);letter-spacing:.5px}
.booking .btn{right:28px;top:12px;width:220px;height:48px;background:var(--green);color:var(--white);font-weight:700;font-size:26px;text-align:center;line-height:48px}
.section-title{width:1200px;text-align:center;font-family:"Cinzel",serif;font-weight:400;font-size:30px;color:var(--blue)}
.see-all{right:128px;font-size:12px;color:var(--muted)}
.services{left:110px;top:1015px;width:980px;height:295px}
.svc{top:0;width:235px;height:295px;text-align:center;padding:26px 18px 0}
.svc .icon{width:54px;height:54px;border-radius:50%;background:#4a4a4a;margin:0 auto 14px}
.svc .icon.leaf{background:var(--green)}
.svc h3{font-size:14px;font-weight:600;margin-bottom:8px;white-space:nowrap}
.svc p{font-size:12.5px;color:var(--muted);text-align:left;line-height:1.45}
.svc .more{position:absolute;left:18px;right:18px;bottom:0;height:36px;line-height:36px;font-size:12px;font-weight:600;border-top:1px solid var(--line)}
.svc.featured{border:2px solid var(--green);box-shadow:0 2px 8px rgba(0,0,0,.1)}
.svc.featured .more{left:0;right:0;background:var(--green);color:var(--white);border:none}
.circle-arrow{width:30px;height:30px;border-radius:50%;border:1px solid #bbb;background:var(--white)}
.video-band{left:0;top:1362px;width:1200px;height:425px;background:linear-gradient(180deg,#5d9fd6 0%,#a9cfee 45%,#e8f1f7 70%,#8fbf4a 88%,#6aa233 100%)}
.video-box{left:542px;top:80px;width:536px;height:308px;background:linear-gradient(160deg,#14213a,#3a2a2a 60%,#0c0c14);border:8px solid var(--white);box-shadow:0 2px 10px rgba(0,0,0,.3)}
.video-box .title{left:14px;top:10px;color:var(--white);font-size:16px}
.video-box .site{right:30px;bottom:14px;color:var(--white);font-size:28px;font-weight:700}
.video-box .play{left:238px;top:118px}
.blog{top:1900px;width:306px;height:365px;border-bottom:1px solid var(--line)}
.blog .photo{width:306px;height:118px}
.blog h4{font-size:15px;font-weight:600;margin:12px 0 8px}
.blog p{font-size:12.5px;color:var(--muted);line-height:1.45}
.blog .by{position:absolute;bottom:10px;width:306px;text-align:center;font-size:12px;color:var(--muted)}
.blog .by b{color:var(--ink)}
.blog.active{background:#d8d8d8;padding:0 12px}
.blog.active .photo{margin:0 -12px}
.blog.active .view{left:0;top:150px;width:306px;height:36px;background:#7aa6c7;color:var(--white);text-align:center;line-height:36px;font-size:14px}
.modules{left:0;top:2323px;width:1200px;height:467px;background:var(--light)}
.big-video{left:118px;top:102px;width:539px;height:312px;background:radial-gradient(ellipse at 55% 55%,#c88a5a 0%,#6a4128 45%,#1d120c 85%)}
.big-video .bar{left:0;bottom:0;width:539px;height:28px;background:rgba(0,0,0,.75)}
.big-video .progress{left:40px;top:12px;width:400px;height:4px;background:#555}
.big-video .progress i{display:block;width:120px;height:4px;background:var(--white)}
.big-video .play{left:235px;top:125px}
.mod-item{left:677px;width:401px;height:145px;background:#d9d9d9;padding:14px}
.mod-item .thumb{left:14px;top:14px;width:160px;height:117px;background:linear-gradient(135deg,#7a4a2e,#d39a6e 55%,#4a2c1c)}
.mod-item p{left:190px;top:14px;width:195px;font-size:12.5px;line-height:1.45;color:var(--ink)}
.newsletter{left:118px;top:2798px;width:967px;height:74px;background:linear-gradient(90deg,#a8d36a,#e7f2d4 40%,#d2e8b0 70%,#a8d36a)}
.newsletter .label{left:20px;top:8px;width:180px;height:58px;background:var(--green);color:#1f3d0a;font-size:22px;font-weight:700;line-height:1.05;padding:6px 0 0 44px}
.newsletter .label span{font-size:27px;display:block}
.newsletter .input{left:300px;top:20px;width:258px;height:34px;background:var(--white);border:1px solid #bbb;font-size:12px;color:#999;padding:8px 10px}
.newsletter .submit{left:572px;top:20px;width:130px;height:34px;background:var(--blue);color:var(--white);font-size:13px;font-weight:700;text-align:center;line-height:34px}
.footer{left:0;top:2912px;width:1200px;height:240px;background:var(--blue);color:var(--white)}
.footer h5{font-size:18px;font-weight:600}
.footer .col{top:22px}
.footer ul{list-style:none;font-size:12.5px;line-height:1.6;margin-top:16px}
.footer .flogo{display:flex;align-items:center;gap:8px;margin-top:18px}
.footer .flogo .dot{width:26px;height:26px;border-radius:50%;background:var(--white)}
.footer .flogo .name{font-size:24px;font-weight:700}
.footer .addr{font-size:12px;line-height:1.55;margin-top:10px}
.social{left:820px;top:0;width:265px;height:240px;background:var(--white);color:var(--ink);padding:16px 14px}
.social h5{font-size:17px;font-weight:700}
.social .card{margin-top:12px;height:110px;border:1px solid var(--line);background:linear-gradient(180deg,#cfe0ea,#f2f6f8)}
.social .card .page{font-size:12px;font-weight:600;color:var(--blue-dark);padding:8px}
.social .card .like{margin:30px 0 0 8px;width:80px;height:22px;border:1px solid #bbb;background:#f6f6f6;font-size:11px;text-align:center;line-height:20px}
.social small{display:block;font-size:11px;color:var(--muted);margin-top:8px}
.copyright{left:0;top:3152px;width:1200px;height:39px;background:var(--white);font-size:11.5px;color:var(--muted);padding:12px 118px}
</style>
</head>
<body>

<div class="abs topbar">
  <span class="abs phone">(555) 214-0187</span>
  <span class="abs sep">|</span>
  <span class="abs contact">Contact us</span>
  <span class="abs cart">
    <svg width="16" height="14" viewBox="0 0 16 14" style="vertical-align:middle"><path d="M1 1h3l2 8h8l1.5-5H5" fill="none" stroke="#fff" stroke-width="1.5"/><circle cx="7" cy="12" r="1.3" fill="#fff"/><circle cx="13" cy="12" r="1.3" fill="#fff"/></svg>
    &nbsp;|&nbsp; 0
  </span>
</div>

<header class="abs header">
  <div class="abs brand">
    <span class="dot"></span>
    <div>
      <div class="name">Bright Oak</div>
      <div class="tag">FAMILY MEDICINE</div>
    </div>
  </div>
  <nav class="abs nav">
    <span class="active">HOME</span><span>ABOUT US</span><span>SERVICES</span><span>RESOURCES</span><span>FAQs</span><span>CURRENT PATIENTS</span><span>LIVEBRIGHT MEMBERSHIP</span><span>STORE</span>
  </nav>
</header>

<section class="abs hero" role="img" aria-label="Photo of a patient relaxing while receiving acupuncture needles on the forehead">
  <h1 class="abs">Live Pain Free<span>Experience Acupuncture</span></h1>
  <svg class="abs arrow" style="left:30px" width="20" height="36" viewBox="0 0 20 36"><path d="M16 2L3 18l13 16" fill="none" stroke="#fff" stroke-width="3"/></svg>
  <svg class="abs arrow" style="right:30px" width="20" height="36" viewBox="0 0 20 36"><path d="M4 2l13 16L4 34" fill="none" stroke="#fff" stroke-width="3"/></svg>
  <div class="abs dots"><i></i><i></i><i></i><i></i><i></i><i></i></div>
</section>

<section class="abs questions">
  <h2 class="abs">Do you have any questions ?</h2>
  <svg class="abs down" width="34" height="34" viewBox="0 0 34 34"><circle cx="17" cy="17" r="15" fill="none" stroke="#2aa3d8" stroke-width="2"/><path d="M10 14l7 7 7-7" fill="none" stroke="#2aa3d8" stroke-width="2.5"/></svg>
</section>

<div class="abs booking">
  <div class="abs text">BOOK YOUR APPOINTMENT WITH NUTRITION</div>
  <div class="abs btn">BOOK NOW</div>
</div>

<h2 class="abs section-title" style="top:912px">Services we Provide</h2>
<span class="abs see-all" style="top:925px">See All</span>

<svg class="abs circle-arrow" style="left:58px;top:1118px" viewBox="0 0 30 30"><path d="M17 9l-6 6 6 6" fill="none" stroke="#999" stroke-width="2"/></svg>
<svg class="abs circle-arrow" style="right:58px;top:1118px" viewBox="0 0 30 30"><path d="M13 9l6 6-6 6" fill="none" stroke="#999" stroke-width="2"/></svg>

<section class="abs services">
  <div class="abs svc" style="left:0">
    <div class="icon"></div>
    <h3>Integrative Family Medicine</h3>
    <p>Lorem ipsum dolor sit amet, consectetuer adipiscing elit, sed diam nonummy nibh euismod tincidunt ut laoreet dolore magna aliquam erat volutpat ut wisi enim ad minim veniam.</p>
    <div class="more">READ MORE</div>
  </div>
  <div class="abs svc featured" style="left:240px">
    <div class="icon leaf"></div>
    <h3>Functional Medicine</h3>
    <p>Lorem ipsum dolor sit amet, consectetuer adipiscing elit, sed diam nonummy nibh euismod tincidunt ut laoreet dolore magna aliquam erat volutpat ut wisi enim ad minim veniam.</p>
    <div class="more">READ MORE</div>
  </div>
  <div class="abs svc" style="left:495px">
    <div class="icon"></div>
    <h3>Nutrition</h3>
    <p>Lorem ipsum dolor sit amet, consectetuer adipiscing elit, sed diam nonummy nibh euismod tincidunt ut laoreet dolore magna aliquam erat volutpat ut wisi enim ad minim veniam.</p>
    <div class="more">READ MORE</div>
  </div>
  <div class="abs svc" style="left:745px">
    <div class="icon"></div>
    <h3>Weight Loss</h3>
    <p>Lorem ipsum dolor sit amet, consectetuer adipiscing elit, sed diam nonummy nibh euismod tincidunt ut laoreet dolore magna aliquam erat volutpat ut wisi enim ad minim veniam.</p>
    <div class="more">READ MORE</div>
  </div>
</section>

<section class="abs video-band" role="img" aria-label="Photo of a woman in white with arms raised in a green field under a blue sky">
  <div class="abs video-box" role="img" aria-label="Practice summary video">
    <div class="abs title">Dan Morrow "Fresh Start" Health and Fitness</div>
    <svg class="abs play" width="60" height="42" viewBox="0 0 60 42"><rect width="60" height="42" rx="8" fill="rgba(0,0,0,.6)"/><path d="M24 12l14 9-14 9z" fill="#fff"/></svg>
    <div class="abs site">DanMorrow.com</div>
  </div>
</section>

<h2 class="abs section-title" style="top:1830px">Latest Blog</h2>
<span class="abs see-all" style="top:1843px">See All Post</span>

<article class="abs blog" style="left:128px">
  <div class="photo" role="img" aria-label="Photo of a relaxing massage" style="background:linear-gradient(120deg,#e9d3c1,#c59a7a 60%,#f3e8de)"></div>
  <h4>diam nonummy nibh euismod</h4>
  <p>Lorem ipsum dolor sit amet, consectetuer adipiscing elit, sed diam nonummy nibh euismod tincidunt ut laoreet dolore magna aliquam erat volutpat ut wisi enim ad minim veniam sed diam nonummy nibh euismod tincidunt ut laoreet dolore magna.</p>
  <div class="by">by <b>Ray Holden</b></div>
</article>
<article class="abs blog active" style="left:447px">
  <div class="photo" role="img" aria-label="Photo of a glowing network of brain cells" style="background:linear-gradient(135deg,#3b5b78,#8fa8bd 50%,#2b4258)"></div>
  <div class="abs view">View Full Blog</div>
  <h4 style="margin-top:14px">sed diam nonummy nibh</h4>
  <p style="margin-top:56px">sed diam nonummy nibh euismod tincidunt ut laoreet dolore magna.</p>
  <div class="by" style="left:0">by <b>Ray Holden</b></div>
</article>
<article class="abs blog" style="left:766px">
  <div class="photo" role="img" aria-label="Photo of hands holding a young green seedling in soil" style="background:linear-gradient(180deg,#f4f6ef,#b8cf8a 55%,#7a5a3a)"></div>
  <h4>euismod tincidunt ut laoreet</h4>
  <p>Lorem ipsum dolor sit amet, consectetuer adipiscing elit, sed diam nonummy nibh euismod tincidunt ut laoreet dolore magna aliquam erat volutpat ut wisi enim ad minim veniam sed diam nonummy nibh euismod tincidunt ut laoreet dolore magna.</p>
  <div class="by">by <b>Ray Holden</b></div>
</article>

<section class="abs modules">
  <h2 class="abs section-title" style="top:34px">Modules for programs online</h2>
  <span class="abs see-all" style="top:48px">See All</span>
  <div class="abs big-video" role="img" aria-label="Video still of acupuncture needles on a patient's back">
    <svg class="abs play" width="70" height="50" viewBox="0 0 70 50"><rect width="70" height="50" rx="8" fill="rgba(0,0,0,.65)"/><path d="M28 14l16 11-16 11z" fill="#fff"/></svg>
    <div class="abs bar">
      <svg class="abs" style="left:14px;top:8px" width="10" height="12" viewBox="0 0 10 12"><path d="M0 0l10 6-10 6z" fill="#fff"/></svg>
      <div class="abs progress"><i></i></div>
    </div>
  </div>
  <div class="abs mod-item" style="top:102px">
    <div class="abs thumb" role="img" aria-label="Video still of a woman during a consultation"></div>
    <p class="abs">euismod tincidunt ut laoreet consectetuer adi piscing elit. Lorem ipsum dolor sit amet, consectetuer adipiscing elit, euismod tincidunt ut laoreet.</p>
  </div>
  <div class="abs mod-item" style="top:269px">
    <div class="abs thumb" role="img" aria-label="Video still of an acupuncture treatment"></div>
    <p class="abs">Lorem ipsum dolor sit amet, consectetuer adipiscing elit, sed diam nonummy euismod tincidunt ut laoreet consectetuer adipiscing elit.</p>
  </div>
</section>

<div class="abs newsletter">
  <div class="abs label">Join Our<span>Newsletter</span></div>
  <div class="abs input">Your E-mail Id</div>
  <div class="abs submit">SUBSCRIBE</div>
</div>

<footer class="abs footer">
  <div class="abs col" style="left:118px">
    <h5>Get in Touch</h5>
    <div class="flogo"><span class="dot"></span><span class="name">Bright Oak</span></div>
    <div class="addr">418 Harlow Lane, Fairmont, TX 70123<br><br>Telephone: (555) 214-0187<br>FAX: (555) 214-0190</div>
  </div>
  <div class="abs col" style="left:365px">
    <h5>Quick Links</h5>
    <ul><li>Home</li><li>About Us</li><li>Services</li><li>Resources</li><li>FAQs</li><li>Current Patients</li><li>LiveBright Membership</li></ul>
  </div>
  <div class="abs col" style="left:515px;top:44px">
    <ul><li>Store</li><li>Contact us</li><li>Sign Up</li><li>Book Appointment</li><li>Questionnaire</li><li>Watch Videos</li><li>Latest Blog</li></ul>
  </div>
  <div class="abs col" style="left:655px;top:44px">
    <ul><li>Shipping</li><li>My Account</li><li>Terms &amp; Conditions</li><li>Privacy Policy</li><li>Legal</li></ul>
  </div>
  <div class="abs social">
    <h5>Like Us on Linkpage</h5>
    <div class="card">
      <div class="page">Bright Oak Family Medicine</div>
      <div class="like">Like Page</div>
    </div>
    <small>Be the first of your friends to like this page</small>
  </div>
</footer>

<div class="abs copyright">Copyright © 2017 brightoakfm.com All Rights Reserved.</div>

</body>
</html>
```